Ardenwell Building and Property Services needs a business card design

We need a business card design for our building and property services business. We already have a logo we just need a creative design and layout on a business card. Emphasis on clean, modern, professional.
Our client targets are mainly body corporates, building managers, construction managers.
We are a building services company that lean more to structural repair of buildings, through concrete rectification and carbon fibre strengthening.
We also refurbish facades, rendering, painting etc
We target higher end body corporates in prestigious locations, hence why we'd like our cards to reflect professionalism, strength, efficiency

Target Market(s)

body corporates, building managers, construction managers

Industry/Entity Type

Construction

Contact Information for Business Card

Ardenwell is the main word, with 'Building and Property Services' underneath.
Level 17, 82 Harlow Street
MERRIDALE
Melbourne
Vic 3094
T: 9518 2736
Duncan Ferris - Director
dunardenwell@mailbox-example.com

Requirements
Must have
• Stand out on the back of the card- strong/ bold, company logo
• All of the contact details written above
Should not have
• I'd like the card to stand out, especially on the back. Id like the company logo to be prominent, although feel free to be creative around it. But remain clean and professional

```html
<!DOCTYPE html>
<html lang="en">
<head>
<meta charset="utf-8">
<title>Ardenwell Building and Property Services – Business Card</title>
<link href="https://fonts.googleapis.com/css2?family=Open+Sans:wght@400;700&display=swap" rel="stylesheet">
<style>
  :root {
    --stage: #2c2c2c;
    --card-white: #ffffff;
    --brand-blue: #1a9fe0;
    --blue-light: #12b6ec;
    --blue-deep: #1673c9;
    --divider-grey: #d4d6d9;
    --ink-grey: #6d6f72;
    --text-on-blue: #ffffff;
  }
  * { margin: 0; padding: 0; box-sizing: border-box; }
  html, body {
    width: 1200px;
    height: 907px;
    overflow: hidden;
    background: var(--stage);
    font-family: "Open Sans", Arial, sans-serif;
  }
  .canvas {
    position: relative;
    width: 1200px;
    height: 907px;
  }
  .card {
    position: absolute;
    top: 305px;
    width: 520px;
    height: 297px;
    background: var(--card-white);
    overflow: hidden;
    box-shadow: 0 8px 24px rgba(0,0,0,0.45);
  }
  .card--front { left: 60px; }
  .card--back  { left: 620px; }

  .contact-panel {
    position: absolute;
    top: 0; right: 0; bottom: 0;
    width: 260px;
    background: linear-gradient(160deg, var(--blue-light) 0%, var(--brand-blue) 50%, var(--blue-deep) 100%);
    clip-path: polygon(22px 0, 100% 0, 100% 100%, 0 100%);
  }
  .divider-band {
    position: absolute;
    top: 0; right: 252px; bottom: 0;
    width: 30px;
    background: linear-gradient(90deg, #f4f5f6, var(--divider-grey));
    clip-path: polygon(22px 0, 30px 0, 8px 100%, 0 100%);
  }
  .contact {
    position: absolute;
    top: 26px;
    right: 22px;
    text-align: right;
    color: var(--text-on-blue);
    font-size: 11.5px;
    line-height: 1.55;
  }
  .contact__name {
    font-weight: 700;
    font-size: 15px;
    letter-spacing: 0.2px;
    text-transform: uppercase;
    line-height: 1.2;
  }
  .contact__role { margin-bottom: 14px; }
  .contact__address { margin-bottom: 12px; }
  .contact__line {
    display: flex;
    justify-content: flex-end;
    align-items: center;
    gap: 5px;
  }
  .contact__line svg { width: 10px; height: 10px; fill: var(--text-on-blue); }

  .brand {
    position: absolute;
    display: flex;
    flex-direction: column;
    align-items: center;
    text-align: center;
  }
  .card--front .brand { left: 0; width: 250px; top: 108px; }
  .card--back .brand  { left: 0; width: 520px; top: 100px; }
  .brand__name {
    font-weight: 400;
    color: var(--brand-blue);
    letter-spacing: 3px;
    text-transform: uppercase;
    display: flex;
    align-items: center;
    gap: 8px;
  }
  .brand__mark {
    display: inline-block;
    background: var(--brand-blue);
  }
  .card--front .brand__name { font-size: 22px; }
  .card--front .brand__mark { width: 12px; height: 12px; }
  .card--back .brand__name { font-size: 38px; letter-spacing: 5px; }
  .card--back .brand__mark { width: 20px; height: 20px; }
  .brand__tagline {
    color: var(--ink-grey);
    text-transform: uppercase;
    letter-spacing: 1px;
    margin-top: 4px;
  }
  .card--front .brand__tagline { font-size: 7.5px; }
  .card--back .brand__tagline { font-size: 12px; letter-spacing: 1.6px; }
</style>
</head>
<body>
<main class="canvas">
  <section class="card card--front" aria-label="Business card front">
    <div class="brand">
      <div class="brand__name"><span class="brand__mark"></span>Ardenwell</div>
      <div class="brand__tagline">Building and Property Services</div>
    </div>
    <div class="divider-band"></div>
    <div class="contact-panel">
      <div class="contact">
        <div class="contact__name">Duncan Ferris</div>
        <div class="contact__role">Director</div>
        <div class="contact__address">Level 17, 82 Harlow Street,<br>MERRIDALE, Melbourne, Vic 3094</div>
        <div class="contact__line">9518 2736
          <svg viewBox="0 0 10 10" aria-hidden="true"><path d="M2 0.5 L3.6 0.5 L4.2 2.8 L3.1 3.6 Q4 5.6 6.2 6.8 L7 5.8 L9.5 6.4 L9.5 8 Q9.5 9.5 8 9.5 Q1 9 0.5 2 Q0.5 0.5 2 0.5 Z"/></svg>
        </div>
        <div class="contact__line">dunardenwell@mailbox-example.com
          <svg viewBox="0 0 10 10" aria-hidden="true"><path d="M0.5 2 H9.5 V8 H0.5 Z M1 2.5 L5 5.6 L9 2.5" fill="none" stroke="#fff" stroke-width="1"/></svg>
        </div>
      </div>
    </div>
  </section>

  <section class="card card--back" aria-label="Business card back">
    <div class="brand">
      <div class="brand__name"><span class="brand__mark"></span>Ardenwell</div>
      <div class="brand__tagline">Building and Property Services</div>
    </div>
  </section>
</main>
</body>
</html>
```